Quorvan - corporate Business Card

We need a good look and innovative business card for a new start up company based in Los Angeles called "Quorvan". We are in a payment business, including payment card, app, and ewallet. We are expert in online payment and Card not present (CNP) transaction.
We need an innovative, modern business card.

Our logo font is Aero Matics

Target Market(s)

Startup - Bank - Online Payment - Card Manufacturing

Industry/Entity Type

Startup

Contact Information for Business Card

phone: 424 555 0173 - Address: 4127 Marlowe blvd, Cylver City, CA 90232

Requirements
Must have
• Message: innovative, professional, expert, high tech, trust, online payment expert, security
Nice to have
• no comment
Should not have
• no Comment

```html
<!DOCTYPE html>
<html lang="en">
<head>
<meta charset="utf-8">
<title>Quorvan – Business Card</title>
<link rel="stylesheet" href="https://fonts.googleapis.com/css2?family=Open+Sans:wght@400;600;700&display=swap">
<style>
  :root {
    --stage: #000000;
    --card-light: #f3f3f3;
    --brand-red: #b31f2e;
    --brand-red-deep: #a91f2c;
    --ink: #333333;
    --white: #ffffff;
  }
  * { margin: 0; padding: 0; box-sizing: border-box; }
  html, body {
    width: 1200px;
    height: 900px;
    overflow: hidden;
    background: var(--stage);
    font-family: "Open Sans", Arial, sans-serif;
  }
  .stage {
    position: relative;
    width: 1200px;
    height: 900px;
  }
  .card {
    position: absolute;
    top: 200px;
    width: 310px;
    height: 502px;
  }
  .card--front {
    left: 265px;
    background: var(--card-light);
    border-radius: 62px 0 72px 0;
  }
  .card--back {
    left: 641px;
    width: 309px;
    background: var(--brand-red-deep);
    border-radius: 0 62px 0 72px;
  }
  .brand {
    position: absolute;
    left: 28px;
    top: 72px;
    display: flex;
    align-items: center;
    gap: 8px;
  }
  .brand__dot {
    width: 78px;
    height: 78px;
    border-radius: 50%;
    background: var(--brand-red);
  }
  .brand__name {
    font-size: 40px;
    font-weight: 600;
    color: var(--brand-red);
    letter-spacing: 0;
    line-height: 1;
    padding-bottom: 6px;
  }
  .person {
    position: absolute;
    left: 28px;
    top: 306px;
  }
  .person__name {
    font-size: 18px;
    font-weight: 700;
    color: var(--brand-red);
    line-height: 24px;
  }
  .person__role {
    font-size: 14px;
    color: var(--ink);
    line-height: 18px;
  }
  .contact {
    position: absolute;
    left: 28px;
    top: 370px;
    list-style: none;
    font-size: 14px;
    color: var(--ink);
    line-height: 19px;
  }
  .contact__item {
    display: flex;
    align-items: center;
    gap: 4px;
  }
  .contact__icon {
    width: 11px;
    height: 11px;
    flex: none;
  }
  .address {
    position: absolute;
    left: 28px;
    top: 426px;
    font-size: 14px;
    font-style: normal;
    color: var(--ink);
    line-height: 19px;
  }
  .back__name {
    position: absolute;
    left: 44px;
    top: 392px;
    font-size: 51px;
    font-weight: 600;
    color: var(--white);
    letter-spacing: 0.5px;
    line-height: 1;
  }
</style>
</head>
<body>
<main class="stage">
  <section class="card card--front" aria-label="Card front">
    <div class="brand">
      <span class="brand__dot"></span>
      <span class="brand__name">quorvan</span>
    </div>

    <div class="person">
      <p class="person__name">Daniel Whitmore</p>
      <p class="person__role">Managing Director</p>
    </div>

    <ul class="contact">
      <li class="contact__item">
        <svg class="contact__icon" viewBox="0 0 12 12" aria-hidden="true">
          <path fill="#b31f2e" d="M2.4 1l2 2.1-1 1.3c.7 1.5 1.8 2.6 3.3 3.3l1.3-1 2.1 2-1.1 1.5C5 10 2 7 .9 2.1z"/>
        </svg>
        <span>424 555 0173</span>
      </li>
      <li class="contact__item">
        <svg class="contact__icon" viewBox="0 0 12 12" aria-hidden="true">
          <circle cx="6" cy="6" r="5.2" fill="#b31f2e"/>
          <path fill="none" stroke="#f3f3f3" stroke-width="0.9" d="M1 6h10M6 .8c-2 2.8-2 7.6 0 10.4M6 .8c2 2.8 2 7.6 0 10.4"/>
        </svg>
        <span>www.quorvan.com</span>
      </li>
    </ul>

    <address class="address">4127 Marlowe blvd,<br>Marden City, CA 90417</address>
  </section>

  <section class="card card--back" aria-label="Card back">
    <p class="back__name">quorvan</p>
  </section>
</main>
</body>
</html>
```